International Legal Service Company needs Letterhead Design

Put my new Logo into Letterhead Design, using updated telephone number, e-mail address and website. Current letterhead and updated information which i want you to include my new letterhead attached herewith. Of course, my new Logo attached herein. Also, you can use slogan "Complete Legal Support Services For Companies Working Worldwide"

It Company

```html
<!DOCTYPE html>
<html lang="en">
<head>
<meta charset="utf-8">
<title>Meridian Counsel Partners Inc — Letterhead</title>
<link href="https://fonts.googleapis.com/css2?family=Questrial&display=swap" rel="stylesheet">
<style>
  :root {
    --backdrop: #d9d9db;
    --paper: #ffffff;
    --brand-navy: #1f2f6b;
    --brand-blue: #2a5fb8;
    --contact-grey: #6e6e72;
    --tagline-grey: #3a3a3e;
  }
  * { margin: 0; padding: 0; box-sizing: border-box; }
  html, body {
    width: 1200px;
    height: 1142px;
    overflow: hidden;
    background: var(--backdrop);
    font-family: "Questrial", "Century Gothic", sans-serif;
  }
  .letterhead {
    position: absolute;
    left: 182px;
    top: 30px;
    width: 836px;
    height: 1082px;
    background: var(--paper);
    box-shadow: 0 6px 24px rgba(0, 0, 0, 0.18);
  }
  .brand {
    position: absolute;
    left: 60px;
    top: 78px;
    display: flex;
    align-items: center;
    gap: 16px;
  }
  .brand-mark {
    width: 82px;
    height: 82px;
    flex: none;
  }
  .brand-name {
    color: var(--brand-navy);
    font-size: 29px;
    line-height: 1.08;
    letter-spacing: 0.2px;
  }
  .tagline {
    position: absolute;
    left: 158px;
    top: 166px;
    font-size: 9px;
    color: var(--tagline-grey);
    letter-spacing: 0.1px;
    white-space: nowrap;
  }
  .contact {
    position: absolute;
    right: 62px;
    top: 52px;
    text-align: right;
    font-size: 14px;
    line-height: 1.3;
    color: var(--contact-grey);
    font-style: normal;
  }
  .contact .label {
    font-size: 9px;
    letter-spacing: 0.5px;
    margin-right: 3px;
  }
</style>
</head>
<body>
  <main class="letterhead">
    <header>
      <div class="brand">
        <svg class="brand-mark" viewBox="0 0 82 82" aria-hidden="true">
          <circle cx="41" cy="41" r="40" fill="var(--brand-blue)"/>
        </svg>
        <div class="brand-name">Meridian Counsel<br>Partners Inc</div>
      </div>
      <p class="tagline">Complete Legal Support Services For Companies Working Worldwide</p>
      <address class="contact">
        1480 Harbor Crest Avenue<br>
        Suite 300<br>
        Lakemont, MD 20990<br>
        <span class="label">TEL</span>240-555-0142<br>
        <span class="label">FAX</span>240-555-0187<br>
        contact@meridiancounsel.com<br>
        www.meridiancounsel.com
      </address>
    </header>
  </main>
</body>
</html>
```